Business Cards

I'd like help creating business cards with the full logo "Veltrona Capital Partners" on the back of the card (navy background with white writing), and abbreviated logo "VCP" on the front. Would like to list name, title, phone number, email, and website listed on front of card. Would like to keep very simple. Front font Arial or similar.

```html
<!DOCTYPE html>
<html lang="en">
<head>
<meta charset="utf-8">
<title>Veltrona Capital Partners – Business Cards</title>
<link rel="stylesheet" href="https://fonts.googleapis.com/css2?family=Arimo:wght@400;700&display=swap">
<style>
  :root {
    --navy: #1d3c6e;
    --navy-deep: #143a6e;
    --navy-light: #3d6aa8;
    --ink-grey: #757575;
    --rule-grey: #8a8a8a;
    --paper: #ffffff;
    --backdrop: #1e1e1e;
  }
  * { margin: 0; padding: 0; box-sizing: border-box; }
  html, body {
    width: 1200px;
    height: 1059px;
    overflow: hidden;
    background: var(--backdrop);
    font-family: "Arimo", Arial, sans-serif;
  }
  .stage {
    position: relative;
    width: 1200px;
    height: 1059px;
  }

  /* Front of card */
  .card-front {
    position: absolute;
    left: 258px;
    top: 89px;
    width: 689px;
    height: 394px;
    background: var(--paper);
  }
  .card-front__frame {
    position: absolute;
    left: 19px;
    top: 19px;
    right: 19px;
    bottom: 19px;
    border: 2px solid var(--navy);
  }
  .identity {
    position: absolute;
    right: 362px;
    top: 174px;
    text-align: right;
  }
  .identity__name {
    font-size: 21px;
    font-weight: 700;
    color: var(--navy);
    letter-spacing: 0.2px;
    line-height: 1.1;
  }
  .identity__title {
    font-size: 18px;
    color: var(--ink-grey);
    line-height: 1.2;
  }
  .card-front__divider {
    position: absolute;
    left: 344px;
    top: 166px;
    width: 1.5px;
    height: 63px;
    background: var(--rule-grey);
  }
  .contact-list {
    position: absolute;
    left: 359px;
    top: 159px;
    list-style: none;
  }
  .contact-list__item {
    display: flex;
    align-items: center;
    height: 25px;
    font-size: 18px;
    color: var(--ink-grey);
  }
  .contact-list__icon {
    width: 16px;
    height: 16px;
    margin-right: 10px;
    flex: none;
  }

  /* Back of card */
  .card-back {
    position: absolute;
    left: 252px;
    top: 541px;
    width: 701px;
    height: 400px;
    overflow: hidden;
  }
  .card-back__pattern {
    position: absolute;
    inset: 0;
    background: linear-gradient(150deg, var(--navy-deep) 0%, var(--navy-deep) 50%, var(--navy-light) 100%);
  }
  .brand-mark {
    position: absolute;
    left: 0;
    right: 0;
    top: 160px;
    text-align: center;
    color: var(--paper);
    font-weight: 700;
  }
  .brand-mark__name {
    display: block;
    font-size: 44px;
    letter-spacing: 3px;
    line-height: 1;
  }
  .brand-mark__tagline {
    display: block;
    margin-top: 10px;
    font-size: 15px;
    letter-spacing: 8px;
  }
</style>
</head>
<body>
<main class="stage">

  <section class="card-front" aria-label="Business card front">
    <div class="card-front__frame"></div>

    <div class="identity">
      <p class="identity__name">DANIEL HARPER</p>
      <p class="identity__title">Manager</p>
    </div>

    <div class="card-front__divider"></div>

    <ul class="contact-list">
      <li class="contact-list__item">
        <svg class="contact-list__icon" viewBox="0 0 24 24" fill="none" stroke="#1d3c6e" stroke-width="2" stroke-linecap="round" stroke-linejoin="round" aria-hidden="true">
          <path d="M5 3h4l2 5-2.5 1.5a11 11 0 0 0 6 6L16 13l5 2v4a2 2 0 0 1-2 2A16 16 0 0 1 3 5a2 2 0 0 1 2-2z"/>
          <path d="M15 3a6 6 0 0 1 6 6"/>
          <path d="M15 7a2 2 0 0 1 2 2"/>
        </svg>
        555-010-2100
      </li>
      <li class="contact-list__item">
        <svg class="contact-list__icon" viewBox="0 0 24 24" fill="none" stroke="#1d3c6e" stroke-width="2" stroke-linejoin="round" aria-hidden="true">
          <rect x="2" y="5" width="20" height="14" rx="2"/>
          <path d="M2 7l10 7 10-7"/>
        </svg>
        dharper@veltronacap.com
      </li>
      <li class="contact-list__item">
        <svg class="contact-list__icon" viewBox="0 0 24 24" fill="none" stroke="#1d3c6e" stroke-width="1.8" aria-hidden="true">
          <circle cx="12" cy="12" r="10"/>
          <ellipse cx="12" cy="12" rx="4.5" ry="10"/>
          <path d="M2 12h20M4 6.5h16M4 17.5h16"/>
        </svg>
        www.veltronacap.com
      </li>
    </ul>
  </section>

  <section class="card-back" aria-label="Business card back">
    <div class="card-back__pattern" role="img" aria-label="Embossed repeating monogram pattern on navy"></div>
    <p class="brand-mark">
      <span class="brand-mark__name">VELTRONA</span>
      <span class="brand-mark__tagline">CAPITAL PARTNERS</span>
    </p>
  </section>

</main>
</body>
</html>
```